Website Design: Neuroscience research lab at an academic University.

I am looking to redo my University website for Neuroscience Research. <br/><br/>I am looking for a clean, modern and organized design to publish our work. Although I want a modern look, the focus should be on the text content.<br/><br/>Pages I need. These pages should be in the navigation bar;<br/>*Home*: with overview of the lab, contact information, and possibly with <br/>"Recent News and Events" information<br/>*Research*/Projects: will have text description, images, as well as video of various research projects we have done or are working on<br/>*People*: Personnel page with photos and bios of the team<br/>*Publications*: List of research articles with hyperlinks to online <br/>versions of articles as well as PDFs<br/>*News*: Continually updated list of events<br/><br/><br/>Some designs I like: <br/><br/>https://www.morvanlabs.example/<br/>http://www.quillarbor.example/<br/>https://tenwicklab.example<br/>http://www.galdrenlab.example/<br/>https://vqom.halbrook.example/

Target Market(s)

Academics, university students, government

Logo Text

Pellory Lab

Number of Pages Required

5+ page

Colors

Designer to choose colors to be used in the design.

Requirements
Must have
• A modern but elegant design that focuses on the research but that is also visually appealing.
• For the logo, please see the sketch in the attached files. That is a rough sketch of a logo that you can base your logo design on.
Should not have
• No search bar

```html
<!DOCTYPE html>
<html lang="en">
<head>
<meta charset="utf-8">
<title>Neuroscience Research Lab</title>
<link href="https://fonts.googleapis.com/css2?family=Lato:ital,wght@0,300;0,400;0,700;1,400&display=swap" rel="stylesheet">
<style>
:root{
  --red:#d9101d;
  --ink:#222;
  --text:#444;
  --muted:#8a8a8a;
  --line:#e2e2e2;
  --panel:#eef2f5;
  --band:#f5f5f5;
  --white:#fff;
}
*{box-sizing:border-box;margin:0;padding:0}
html,body{width:1200px;height:3446px;overflow:hidden}
body{font-family:'Lato',sans-serif;color:var(--text);background:var(--white);position:relative}
h1,h2,h3,h4{font-weight:400}
.abs{position:absolute}
a{color:inherit;text-decoration:none}

.hero{position:absolute;left:0;top:0;width:1200px;height:601px;overflow:hidden}
.hero-photo{position:absolute;inset:0;background:linear-gradient(120deg,#5b5b5b 0%,#7a7a7a 45%,#4d4d4d 100%)}
.hero-shape{position:absolute;left:0;top:0}
.logo{left:160px;top:36px;color:var(--white);font-size:22px;font-weight:700;letter-spacing:.5px}
.nav{left:452px;top:43px;display:flex;gap:26px;color:var(--white);font-size:11.5px;font-weight:700;text-transform:uppercase}
.nav span.drop::after{content:"";display:inline-block;width:4px;height:4px;border-right:1px solid #fff;border-bottom:1px solid #fff;transform:rotate(45deg);margin:0 0 3px 5px}
.hero-title{left:161px;top:178px;color:var(--white);font-size:30px;font-weight:700;line-height:38px}
.hero-text{left:161px;top:278px;width:355px;color:var(--white);font-size:11.5px;line-height:22.5px}
.btn-outline{left:161px;top:370px;width:114px;height:45px;background:var(--white);color:var(--red);font-size:12px;display:flex;align-items:center;justify-content:center;border-radius:2px}
.arrow{width:52px;height:52px;display:flex;align-items:center;justify-content:center}
.arrow.prev{left:890px;top:310px;background:var(--white)}
.arrow.next{left:950px;top:363px;background:var(--red)}

.about-title{left:161px;top:673px;font-size:17.5px;color:var(--ink)}
.about-body{left:161px;top:718px;width:205px;font-size:11px;line-height:22.5px;color:var(--text)}
.about-body p{margin-bottom:6px}
.about-body ul{list-style:none;margin:14px 0 14px}
.about-body li{position:relative;padding-left:22px;font-size:9.5px;line-height:18px;margin-bottom:4px}
.about-body li::before{content:"";position:absolute;left:0;top:4px;width:11px;height:11px;border-radius:50%;background:#ddd}
.view-all{left:161px;top:1126px;font-size:11px;color:var(--red);text-decoration:underline}
.pub-card{left:385px;top:686px;width:654px;height:457px;background:var(--panel);box-shadow:0 6px 18px rgba(0,0,0,.12)}
.pub{position:absolute;left:45px;width:560px}
.pub-icon{position:absolute;left:0;top:4px;width:38px;height:38px;border:1.5px solid var(--red);border-radius:50%;display:flex;align-items:center;justify-content:center}
.pub h4{margin-left:53px;font-size:12.5px;color:var(--ink)}
.pub .authors{margin-left:53px;margin-top:5px;font-style:italic;font-size:9.5px;color:var(--text)}
.pub .link{margin-left:53px;margin-top:12px;font-style:italic;font-size:9.5px;color:var(--text);display:flex;align-items:center;gap:9px}
.pub .link i{width:8px;height:8px;border:1px solid #555;display:inline-block}

.band{left:0;top:1217px;width:1200px;height:628px;background:var(--band)}
.section-title{position:absolute;left:0;width:1200px;text-align:center;font-size:17.5px;color:var(--ink);display:flex;justify-content:center;align-items:center;gap:14px;text-transform:uppercase}
.section-title::before,.section-title::after{content:"";width:38px;height:1.5px;background:var(--red)}
.tabs{left:161px;top:1350px;width:878px;height:58px;background:var(--white);display:flex}
.tab{flex:1;display:flex;align-items:center;justify-content:center;font-size:15px;color:var(--ink);position:relative}
.tab.active::before,.tab.active::after{content:"";position:absolute;left:50%;transform:translateX(-50%);width:134px;height:2px;background:var(--red)}
.tab.active::before{top:0}.tab.active::after{bottom:0}
.svc-title{left:161px;top:1492px;font-size:21px;color:var(--ink)}
.svc-text{left:161px;top:1542px;width:430px;font-size:11px;line-height:22.5px}
.btn-red{left:161px;top:1695px;width:114px;height:45px;background:var(--red);color:var(--white);font-size:12px;font-weight:700;display:flex;align-items:center;justify-content:center;border-radius:2px}
.svc-image{left:611px;top:1468px;width:428px;height:300px;background:linear-gradient(135deg,#2f4a6e,#8fa3b5 55%,#1c2a3a)}

.card{width:278px;height:248px;border:1px solid var(--line);background:var(--white);text-align:center}
.card.lifted{box-shadow:0 8px 18px rgba(0,0,0,.12)}
.card svg{margin-top:40px}
.card h3{margin-top:10px;font-size:14px;font-weight:700;color:var(--ink)}
.card hr{width:38px;border:0;height:1.5px;background:var(--red);margin:12px auto 14px}
.card p{font-size:11px;line-height:22.5px;color:var(--text);padding:0 40px}

.area{width:203px;top:2580px}
.area h3{text-align:center;font-size:17px;color:var(--ink)}
.area .sub{text-align:center;font-size:11.5px;line-height:15px;color:var(--muted);margin-top:20px;padding-bottom:16px;border-bottom:1px solid var(--line)}
.area li{list-style:none;font-size:10px;color:var(--red);height:35px;line-height:34px;border-bottom:1px solid var(--line)}

.latest-text{left:230px;top:2933px;width:740px;text-align:center;font-size:11px;line-height:22.5px}
.video{left:311px;top:3033px;width:578px;height:299px;background:linear-gradient(135deg,#b9b3ab,#d9cdb9 45%,#c68a2a 60%,#8d8379)}
.play{left:560px;top:3143px;width:80px;height:80px;border-radius:50%;background:var(--red);display:flex;align-items:center;justify-content:center}
</style>
</head>
<body>

<header class="hero">
  <div class="hero-photo" role="img" aria-label="Photo of a researcher looking into a laboratory microscope"></div>
  <svg class="hero-shape" width="1200" height="601" viewBox="0 0 1200 601">
    <path d="M0 0 H600 C520 120 560 200 570 330 C580 460 540 540 500 601 H0 Z" fill="#d9101d"/>
  </svg>
  <div class="abs logo">LOGO GOES HERE</div>
  <nav class="abs nav">
    <a>Home</a><span class="drop">Recent News and Events</span><span class="drop">Research/Projects</span><a>Team</a><span class="drop">Publications</span><a>News</a>
  </nav>
  <h1 class="abs hero-title">Lorem Ipsum Dolor<br>amet palst &amp; healthy</h1>
  <p class="abs hero-text">Lorem ipsum dolor amet palst roof party everyday carry migas pop-up. Freegan ethical shabby chic tote, letterpress pork belly afti .austin synth migas typewriter 90's adaptogen sriracha literally XOXO</p>
  <a class="abs btn-outline">CONTACT US</a>
  <div class="abs arrow prev"><svg width="24" height="14"><path d="M23 7H2M8 1L2 7l6 6" stroke="#d9101d" stroke-width="1.6" fill="none"/></svg></div>
  <div class="abs arrow next"><svg width="24" height="14"><path d="M1 7h21M16 1l6 6-6 6" stroke="#fff" stroke-width="1.6" fill="none"/></svg></div>
</header>

<section>
  <h2 class="abs about-title">About Publications Group</h2>
  <div class="abs about-body">
    <p>Vegan echo park succulents, flexitarian intelligentsia palst disrupt slow-carboni deep v narwhal wayfarers tbh</p>
    <p>Vegan echo park succulents, flexitarian intelligentsia palst disrupt slow-carb deep v narwhal wayfarers tbh. Squid four lomo pickled woke, jianbing handset zine. Leggings woke bespoke, chichar-.rones enamel pin cliche green juice</p>
    <ul>
      <li>Lorem ipsum dolor amet palst roof of a party everyday carry migas pop-up</li>
      <li>Lorem ipsum dolor amet palst roof of a</li>
      <li>Lorem ipsum dolor amet palst roof of a</li>
    </ul>
    <p>Vegan echo park succulents, flexitarian intelligentsia palst disrupt slow-carboni lorem ipsum dolor amet ningun postedi</p>
  </div>
  <a class="abs view-all">View All Publications</a>

  <div class="abs pub-card">
    <div class="pub" style="top:56px">
      <div class="pub-icon"><svg width="16" height="18"><rect x="4" y="2" width="9" height="12" fill="none" stroke="#d9101d"/><path d="M2 5v11h9M6 6h5M6 9h5" stroke="#d9101d" fill="none"/></svg></div>
      <h4>Halvern bulb brenstaard authentic art party you probably haven't any if</h4>
      <div class="authors">A.Ledrow, K.K.A, Lorem Ipsum Dolor.K.S Dolor Valarg Morthulis [241]</div>
      <div class="link"><i></i>Check Publisher's Website Here</div>
    </div>
    <div class="pub" style="top:155px">
      <div class="pub-icon"><svg width="16" height="18"><rect x="4" y="2" width="9" height="12" fill="none" stroke="#d9101d"/><path d="M2 5v11h9M6 6h5M6 9h5" stroke="#d9101d" fill="none"/></svg></div>
      <h4>Halvern bulb brenstaard authentic art party you probably haven't any if</h4>
      <div class="authors">A.Ledrow, K.K.A, Lorem Ipsum Dolor.K.S Dolor Valarg Morthulis [241]</div>
      <div class="link"><i></i>Check Publisher's Website Here</div>
    </div>
    <div class="pub" style="top:254px">
      <div class="pub-icon"><svg width="16" height="18"><rect x="4" y="2" width="9" height="12" fill="none" stroke="#d9101d"/><path d="M2 5v11h9M6 6h5M6 9h5" stroke="#d9101d" fill="none"/></svg></div>
      <h4>Halvern bulb brenstaard authentic art party you probably haven't any if</h4>
      <div class="authors">A.Ledrow, K.K.A, Lorem Ipsum Dolor.K.S Dolor Valarg Morthulis [241]</div>
      <div class="link"><i></i>Check Publisher's Website Here</div>
    </div>
    <div class="pub" style="top:353px">
      <div class="pub-icon"><svg width="16" height="18"><rect x="4" y="2" width="9" height="12" fill="none" stroke="#d9101d"/><path d="M2 5v11h9M6 6h5M6 9h5" stroke="#d9101d" fill="none"/></svg></div>
      <h4>Halvern bulb brenstaard authentic art party you probably haven't any if</h4>
      <div class="authors">A.Ledrow, K.K.A, Lorem Ipsum Dolor.K.S Dolor Valarg Morthulis [241]</div>
      <div class="link"><i></i>Check Publisher's Website Here</div>
    </div>
  </div>
</section>

<section>
  <div class="abs band"></div>
  <h2 class="section-title" style="top:1289px">Services</h2>
  <div class="abs tabs">
    <div class="tab">Lorem Ipsum Dolor</div>
    <div class="tab active">Dolor Amet Ningun</div>
    <div class="tab">Cancer Researches</div>
    <div class="tab">Experimentionals</div>
  </div>
  <h3 class="abs svc-title">Lorem Ipsum Dolor Manganis</h3>
  <p class="abs svc-text">Excepteur sint occaecat cupidatat non proident sunt in culpa qui officia desunt mollit anim id est laborum. sed ut per spiciatis unde omnis natus error vitae Inventore verita-tis quasi architebeatae vitae dicta sunt explicabo nemo enim ipsam voluptatem quia voluptassit.aspernatur aut odit aut fugit sed quia eos consequntur magni dolores eos qui ratione</p>
  <a class="abs btn-red">READ MORE</a>
  <div class="abs svc-image" role="img" aria-label="Row of laboratory microscopes on a bench"></div>
</section>

<section>
  <div class="abs card lifted" style="left:161px;top:1920px">
    <svg width="46" height="44" viewBox="0 0 46 44"><path d="M23 40C8 28 3 21 3 13A10 10 0 0 1 23 9a10 10 0 0 1 20 4c0 8-5 15-20 27z" fill="none" stroke="#d9101d" stroke-width="2"/><path d="M8 20h8l3-5 4 9 3-6h12" fill="none" stroke="#d9101d" stroke-width="1.6"/></svg>
    <h3>Lorem Ipsum Dolor Amet</h3><hr>
    <p>Waistcoat chambray swag, cloud bread mumblecore slow-carb  more ashosete squid, retro banh mi pork</p>
  </div>
  <div class="abs card" style="left:461px;top:1920px">
    <svg width="46" height="46" viewBox="0 0 46 46"><path d="M17 3h12M19 3v14L5 41h36L27 17V3" fill="none" stroke="#d9101d" stroke-width="2"/><circle cx="18" cy="33" r="2.5" fill="#d9101d"/><circle cx="27" cy="35" r="2" fill="#d9101d"/><circle cx="24" cy="28" r="1.8" fill="#d9101d"/></svg>
    <h3>Dolor Amet Lorem</h3><hr>
    <p>Waistcoat chambray swag, cloud bread mumblecore slow-carb  more ashosete squid, retro banh mi pork</p>
  </div>
  <div class="abs card" style="left:761px;top:1920px">
    <svg width="46" height="46" viewBox="0 0 46 46"><path d="M23 29L8 15a7 7 0 0 1 10-10l5 5 5-5a7 7 0 0 1 10 10z" fill="none" stroke="#d9101d" stroke-width="2"/><path d="M16 9l14 14" stroke="#d9101d" stroke-width="2"/><circle cx="20" cy="35" r="2" fill="none" stroke="#d9101d"/><circle cx="26" cy="36" r="2" fill="none" stroke="#d9101d"/><circle cx="23" cy="42" r="2" fill="none" stroke="#d9101d"/></svg>
    <h3>Ipsum Lorem Text</h3><hr>
    <p>Waistcoat chambray swag, cloud bread mumblecore slow-carb  more ashosete squid, retro banh mi pork</p>
  </div>
  <div class="abs card" style="left:161px;top:2192px">
    <svg width="46" height="46" viewBox="0 0 46 46"><path d="M15 3h16M18 3v34a5 5 0 0 0 10 0V3M18 20h10" fill="none" stroke="#d9101d" stroke-width="2"/></svg>
    <h3>Lorem Ipsum Dolor Amet</h3><hr>
    <p>Waistcoat chambray swag, cloud bread mumblecore slow-carb  more ashosete squid, retro banh mi pork</p>
  </div>
  <div class="abs card" style="left:461px;top:2192px">
    <svg width="46" height="46" viewBox="0 0 46 46"><path d="M4 44V24h38v20zM10 24V4M10 4h6v34h-6M20 4h6v34h-6M30 4h6v34h-6" fill="none" stroke="#d9101d" stroke-width="2"/></svg>
    <h3>Lorem Ipsum Dolor Amet</h3><hr>
    <p>Waistcoat chambray swag, cloud bread mumblecore slow-carb  more ashosete squid, retro banh mi pork</p>
  </div>
  <div class="abs card" style="left:761px;top:2192px">
    <svg width="46" height="46" viewBox="0 0 46 46"><rect x="9" y="9" width="28" height="34" rx="2" fill="none" stroke="#d9101d" stroke-width="2"/><path d="M12 3h22v6H12zM20 19h6v5h5v6h-5v5h-6v-5h-5v-6h5z" fill="none" stroke="#d9101d" stroke-width="2"/></svg>
    <h3>Lorem Ipsum Dolor Amet</h3><hr>
    <p>Waistcoat chambray swag, cloud bread mumblecore slow-carb  more ashosete squid, retro banh mi pork</p>
  </div>
</section>

<section>
  <h2 class="section-title" style="top:2510px">Research Areas</h2>
  <div class="abs area" style="left:161px">
    <h3>Antibody Study</h3>
    <div class="sub">Bone If Turnover Markers for use in Biological Research</div>
    <ul><li>Lorem Ipsum Dolor Amet</li><li>Valar Dohenis Postedam X-ray brooklyn</li><li>Stimmy Text Is Siimply Dummy</li><li>Dolor Amet Ningun Yolo</li></ul>
  </div>
  <div class="abs area" style="left:386px">
    <h3>Bacteria Study</h3>
    <div class="sub">Bone If Turnover Markers for use in Biological Research</div>
    <ul><li>Lorem Ipsum Dolor Amet</li><li>Valar Dohenis Postedam X-ray brooklyn</li><li>Stimmy Text Is Siimply Dummy</li><li>Dolor Amet Ningun Yolo</li></ul>
  </div>
  <div class="abs area" style="left:611px">
    <h3>Experimental Research</h3>
    <div class="sub">Bone If Turnover Markers for use in Biological Research</div>
    <ul><li>Lorem Ipsum Dolor Amet</li><li>Valar Dohenis Postedam X-ray brooklyn</li><li>Stimmy Text Is Siimply Dummy</li><li>Dolor Amet Ningun Yolo</li></ul>
  </div>
  <div class="abs area" style="left:836px">
    <h3>Other Researches</h3>
    <div class="sub">Bone If Turnover Markers for use in Biological Research</div>
    <ul><li>Lorem Ipsum Dolor Amet</li><li>Valar Dohenis Postedam X-ray brooklyn</li><li>Stimmy Text Is Siimply Dummy</li><li>Dolor Amet Ningun Yolo</li></ul>
  </div>
</section>

<section>
  <h2 class="section-title" style="top:2891px">Latest Research: The Bacteria Behind Food Poisoning</h2>
  <p class="abs latest-text">Lorem ipsum dolor amet four dollar toast put a bird on it viral hell of listicle, chillwave quinoa intelligentsia slow-carb twee enamel pin. You proba-bly haven't heard of them tousled plaid pour-over tote bag. Small batch tbh subway tile taiyaki</p>
  <div class="abs video" role="img" aria-label="Video still of a lab sample bowl with yellow culture and small jars"></div>
  <div class="abs play"><svg width="26" height="28"><path d="M4 2l20 12L4 26z" fill="#fff"/></svg></div>
</section>

</body>
</html>
```